Business Card Design (NEW FILES)

ATTENTION: New vector files are available. Please update your design to reflect/use the new (better resolution) logo images.

Seeking a unique and professional business card design for a commercial drone photography/videography business. The layout should feature
the logo (attached) and include the following information:
978-512-6037
www.skyvantmedia.com
ORD Certified Remote Pilot

```html
<!DOCTYPE html>
<html lang="en">
<head>
<meta charset="utf-8">
<title>Skyvant Media – Business Card</title>
<link rel="stylesheet" href="https://fonts.googleapis.com/css2?family=Montserrat:wght@400;500;800&display=swap">
<style>
  :root {
    --page-bg: #c9c9c9;
    --card-bg: #ffffff;
    --navy: #25244f;
    --orange: #e9894a;
    --ink: #2b2a52;
  }
  * { margin: 0; padding: 0; box-sizing: border-box; }
  html, body {
    width: 1200px; height: 900px; overflow: hidden;
    background: var(--page-bg);
    font-family: "Montserrat", Arial, sans-serif;
    color: var(--ink);
  }
  .sheet {
    position: relative; width: 1200px; height: 900px;
    display: flex; flex-direction: column; align-items: center;
    justify-content: center; gap: 44px;
  }
  .card {
    position: relative;
    width: 700px; height: 400px;
    background: var(--card-bg);
    border-radius: 28px;
    border-bottom: 6px solid var(--navy);
    box-shadow: 0 6px 18px rgba(0,0,0,0.18);
  }
  .brand {
    display: flex; align-items: center; gap: 14px;
  }
  .brand-dot {
    width: 22px; height: 22px; border-radius: 50%;
    background: var(--orange);
  }
  .brand-name {
    font-weight: 500; color: var(--navy);
    letter-spacing: 0.02em; text-transform: uppercase;
  }
  .card-front .brand {
    position: absolute; left: 50%; top: 50%;
    transform: translate(-50%, -50%);
  }
  .card-front .brand-name { font-size: 46px; }
  .card-back .brand {
    position: absolute; right: 48px; top: 58px;
  }
  .card-back .brand-name { font-size: 32px; }
  .card-back .brand-dot { width: 16px; height: 16px; }
  .holder {
    position: absolute; left: 48px; top: 58px;
  }
  .holder-name { font-size: 30px; font-weight: 800; color: var(--navy); }
  .holder-role { font-size: 16px; font-weight: 400; margin-top: 2px; }
  .credentials {
    position: absolute; left: 48px; bottom: 150px;
    font-size: 17px; line-height: 1.3;
  }
  .contacts {
    position: absolute; left: 48px; bottom: 38px;
    list-style: none; font-size: 17px;
  }
  .contacts li {
    display: flex; align-items: center; gap: 14px; line-height: 30px;
  }
  .contacts svg { width: 16px; height: 16px; fill: var(--navy); }
</style>
</head>
<body>
<main class="sheet">
  <section class="card card-front">
    <div class="brand">
      <span class="brand-dot"></span>
      <span class="brand-name">Skyvant Media</span>
    </div>
  </section>

  <section class="card card-back">
    <div class="holder">
      <p class="holder-name">Mark Doyle</p>
      <p class="holder-role">Owner</p>
    </div>
    <div class="brand">
      <span class="brand-dot"></span>
      <span class="brand-name">Skyvant Media</span>
    </div>
    <div class="credentials">
      <p>ORD Certified Remote Pilot</p>
      <p>Fully Insured</p>
    </div>
    <ul class="contacts">
      <li>
        <svg viewBox="0 0 16 16" aria-hidden="true"><path d="M3 1h3l1.5 3.5-2 1.2a9 9 0 0 0 4.8 4.8l1.2-2L15 10v3a2 2 0 0 1-2 2A12 12 0 0 1 1 3a2 2 0 0 1 2-2z"/></svg>
        <span>978-512-6037</span>
      </li>
      <li>
        <svg viewBox="0 0 16 16" aria-hidden="true"><path d="M1 3h14v10H1z M1.8 3.8 8 8.6l6.2-4.8" fill="none" stroke="#25244f" stroke-width="1.6"/></svg>
        <span>info@skyvantmedia.com</span>
      </li>
      <li>
        <svg viewBox="0 0 16 16" aria-hidden="true"><circle cx="8" cy="8" r="6.5" fill="none" stroke="#25244f" stroke-width="1.5"/><path d="M1.5 8h13M8 1.5c-3 3.5-3 9.5 0 13M8 1.5c3 3.5 3 9.5 0 13" fill="none" stroke="#25244f" stroke-width="1.2"/></svg>
        <span>www.skyvantmedia.com</span>
      </li>
    </ul>
  </section>
</main>
</body>
</html>
```